Statement on the current financial and economic crisis, with a focus on Greece,

Anybody can become angry - that is easy, but to be angry with the right person and to the right degree and at the right time and for the right purpose, and in the right way - that is not within everybody's power and is not easy.
(Thessidor ) greek philosopher

i want to do a poster with this words from Thessidor greek philosopher and to show this statement for the greek people... its about for my project that i am doing.
Updates

Target Market(s)

my audience will be greek people but not only, from 18-80 years old for that reason i want my statement to be in english.

Industry/Entity Type

Financial

Requirements
Must have
• Anybody can become angry - that is easy, but to be angry with the right person and to the right degree and at the right time and for the right purpose, and in the right way - that is not within everybody's power and is not easy.
i want to show in my poster this statement from:
Thessidor greek philosopher (384 – 322 BC)

```html
<!DOCTYPE html>
<html lang="en">
<head>
<meta charset="utf-8">
<title>Thessidor – On Anger</title>
<link rel="stylesheet" href="https://fonts.googleapis.com/css2?family=Mukta:wght@700;800&display=swap">
<style>
  :root {
    --sky-teal: #6fc5cf;
    --sky-deep: #5fbcc8;
    --cloud-light: #d3e4e6;
    --cloud-mid: #a9d6dc;
    --ink: #545a5f;
  }
  html, body {
    margin: 0;
    padding: 0;
    overflow: hidden;
    background: #ffffff;
  }
  .poster {
    position: relative;
    width: 1200px;
    height: 839px;
    overflow: hidden;
    background: var(--sky-teal);
    font-family: "Mukta", sans-serif;
  }
  .sky-backdrop {
    position: absolute;
    inset: 0;
    background:
      radial-gradient(ellipse 170px 330px at 290px 560px, var(--cloud-light) 0%, rgba(211,228,230,0.6) 45%, rgba(211,228,230,0) 100%),
      radial-gradient(ellipse 220px 140px at 520px 250px, rgba(211,228,230,0.85) 0%, rgba(211,228,230,0) 100%),
      radial-gradient(ellipse 160px 110px at 470px 380px, rgba(211,228,230,0.7) 0%, rgba(211,228,230,0) 100%),
      radial-gradient(ellipse 260px 160px at 90px 760px, rgba(169,214,220,0.9) 0%, rgba(169,214,220,0) 100%),
      radial-gradient(ellipse 200px 120px at 760px 60px, rgba(169,214,220,0.8) 0%, rgba(169,214,220,0) 100%),
      radial-gradient(ellipse 300px 200px at 1050px 150px, rgba(95,188,200,0.9) 0%, rgba(95,188,200,0) 100%),
      linear-gradient(135deg, var(--sky-teal) 0%, var(--sky-deep) 100%);
  }
  .quote {
    position: absolute;
    left: 524px;
    top: 450px;
    margin: 0;
    color: var(--ink);
    font-weight: 800;
    font-size: 25.5px;
    line-height: 33px;
    letter-spacing: 0.1px;
  }
  .quote-line {
    display: block;
    white-space: nowrap;
  }
  .attribution {
    position: absolute;
    right: 79px;
    top: 696px;
    margin: 0;
    color: var(--ink);
    font-weight: 800;
    white-space: nowrap;
  }
  .attribution-name {
    font-size: 25.5px;
  }
  .attribution-role {
    font-size: 17px;
    font-weight: 700;
  }
</style>
</head>
<body>
  <main class="poster">
    <div class="sky-backdrop" role="img" aria-label="Halftone-printed teal sky with soft pale clouds"></div>

    <p class="quote">
      <span class="quote-line">Anybody can become angry - that is easy,</span>
      <span class="quote-line">but to be angry with the right person</span>
      <span class="quote-line">and to the right degree</span>
      <span class="quote-line">and at the right purpose,</span>
      <span class="quote-line">and in the right way -</span>
      <span class="quote-line">that is not within everybody’s power</span>
      <span class="quote-line">and is not easy.</span>
    </p>

    <p class="attribution">
      <span class="attribution-name">Thessidor</span>
      <span class="attribution-role">(greek philosopher)</span>
    </p>
  </main>
</body>
</html>
```